Business Card Design

Psychotherapy and Therapeutic Counselling

As well as Life Coaching.

Ember
Life Coaching Services
Confidential and Compassionate
XW FdSc Qualified Practitioner

Tel 07700900482

```html
<!DOCTYPE html>
<html lang="en">
<head>
<meta charset="utf-8">
<title>Ember Psychotherapy – Business Card</title>
<link href="https://fonts.googleapis.com/css2?family=Almendra+SC&family=Architects+Daughter&family=Audiowide&family=Roboto+Condensed:wght@700&display=swap" rel="stylesheet">
<style>
  :root {
    --page-bg: #e9e9ec;
    --band-deep: #2b2596;
    --band-mid: #3a3bc0;
    --band-light: #5a63d8;
    --sky-top: #3f8fdc;
    --sky-mid: #8cc3f0;
    --sky-glow: #dff0fd;
    --divider: #9fd8f5;
    --text-white: #ffffff;
    --text-cyan: #7fd6f7;
    --pill-dark: #7a3716;
    --pill-light: #b4623a;
  }
  * { margin: 0; padding: 0; box-sizing: border-box; }
  html, body {
    width: 1200px;
    height: 1200px;
    overflow: hidden;
    background: var(--page-bg);
  }
  .canvas {
    width: 1200px;
    height: 1200px;
    display: flex;
    align-items: center;
    justify-content: center;
  }
  .business-card {
    position: relative;
    width: 1040px;
    height: 600px;
    overflow: hidden;
    background: var(--band-mid);
    box-shadow: 0 10px 30px rgba(0, 0, 0, 0.18);
  }
  .card-shapes,
  .hero-photo {
    position: absolute;
    left: 0;
    top: 0;
    width: 1040px;
    height: 600px;
  }
  .practice-title {
    position: absolute;
    top: 26px;
    left: 150px;
    right: 30px;
    text-align: center;
    font-family: "Almendra SC", serif;
    font-weight: 400;
    font-size: 31px;
    line-height: 44px;
    color: var(--text-white);
    letter-spacing: 0.5px;
  }
  .practice-title .line-two {
    display: block;
    padding-left: 70px;
  }
  .contact-copy {
    position: absolute;
    left: 36px;
    top: 452px;
    width: 480px;
  }
  .tagline {
    font-family: "Architects Daughter", cursive;
    font-size: 25px;
    line-height: 40px;
    color: var(--text-white);
    text-transform: uppercase;
    white-space: nowrap;
  }
  .credential {
    margin-top: 18px;
    margin-left: 8px;
    font-family: "Audiowide", sans-serif;
    font-size: 18px;
    line-height: 26px;
    color: var(--text-cyan);
    letter-spacing: 0.5px;
    text-transform: uppercase;
    white-space: nowrap;
  }
  .phone-pill {
    position: absolute;
    left: 545px;
    top: 448px;
    width: 465px;
    height: 124px;
    border-radius: 62px;
    border: 4px solid var(--text-white);
    background: linear-gradient(180deg, var(--pill-light) 0%, var(--pill-dark) 100%);
    display: flex;
    align-items: center;
    padding-left: 36px;
    gap: 24px;
  }
  .phone-icon {
    width: 62px;
    height: 62px;
    flex: none;
  }
  .phone-number {
    font-family: "Roboto Condensed", sans-serif;
    font-weight: 700;
    font-size: 52px;
    color: var(--text-white);
    letter-spacing: 1px;
    white-space: nowrap;
  }
</style>
</head>
<body>
<main class="canvas">
  <article class="business-card">
    <svg class="card-shapes" viewBox="0 0 1040 600" aria-hidden="true">
      <defs>
        <linearGradient id="band-gradient" x1="0" y1="0" x2="1" y2="1">
          <stop offset="0" stop-color="var(--band-light)"/>
          <stop offset="0.5" stop-color="var(--band-mid)"/>
          <stop offset="1" stop-color="var(--band-deep)"/>
        </linearGradient>
      </defs>
      <rect width="1040" height="600" fill="url(#band-gradient)"/>
      <path d="M0,150 Q560,90 1040,190 L1040,240 Q600,130 0,170 Z" fill="var(--band-deep)" opacity="0.5"/>
    </svg>

    <svg class="hero-photo" viewBox="0 0 1040 600" role="img" aria-label="Photograph of a man seen from behind with arms outstretched against a bright blue sky with white clouds">
      <defs>
        <radialGradient id="sky-gradient" cx="0.45" cy="0.35" r="0.75">
          <stop offset="0" stop-color="var(--sky-glow)"/>
          <stop offset="0.35" stop-color="var(--sky-mid)"/>
          <stop offset="1" stop-color="var(--sky-top)"/>
        </radialGradient>
      </defs>
      <path d="M0,175 Q560,105 1040,230 L1040,412 L0,412 Z" fill="url(#sky-gradient)"/>
      <rect x="0" y="410" width="1040" height="4" fill="var(--divider)"/>
    </svg>

    <h1 class="practice-title">
      Ember Psychotherapy and Therapeutic Counselling
      <span class="line-two">Life Coaching Services</span>
    </h1>

    <div class="contact-copy">
      <p class="tagline">Confidential and Compassionate</p>
      <p class="credential">XW FdSc Qualified Practitioner</p>
    </div>

    <div class="phone-pill">
      <svg class="phone-icon" viewBox="0 0 64 64" aria-hidden="true">
        <path d="M6,22 C6,12 18,8 32,8 C46,8 58,12 58,22 L58,26 L45,26 L45,19 C40,17 24,17 19,19 L19,26 L6,26 Z" fill="var(--text-white)"/>
        <path d="M20,28 L44,28 L54,52 C54,55 52,57 49,57 L15,57 C12,57 10,55 10,52 Z" fill="var(--text-white)"/>
        <circle cx="32" cy="42" r="8" fill="var(--pill-dark)"/>
        <circle cx="32" cy="42" r="3" fill="var(--text-white)"/>
      </svg>
      <span class="phone-number">07700900482</span>
    </div>
  </article>
</main>
</body>
</html>
```